Healthy Food Healthy Brain Rack Card

We want a new 2 page (front and page) 3.67" x 8.5" rack card. This rack card is the first of a series we are creating. We will have five more eventually.

The minimum font size for the text on the front is 11 point and also for other main body text.

Use the text on the word document.

The images and layout in the word document are just sample ideas we had.

We have a subscripton to pelvane stock images so prefer to get images from there or free high quality images.

The document is for older readers. Do not put text over graphics and keep it simple and easy to read with high contrast.

We are open to any color scheme, though something that conveys fresh and healthy, is good.

We want some very simple design element(s) incorporated that convey Native American communities or heritage. But NO head dress, teepee graphics, etc.

At the top, of the first page we would like a collage of healthy food images. This can include fish, chicken, fresh vegetables, berries, brown rice, etc.

On the back side, the text below the brown box on the word document with the title "mock up" can be smaller as needed.

Please remember to include the funding statement - it can be in a very small font 6/7 point.

For more information about our project, please visit https://morvetlin.org/brain-health/

```html
<!DOCTYPE html>
<html lang="en">
<head>
<meta charset="utf-8">
<title>Healthy Food Healthy Brain Rack Card</title>
<link href="https://fonts.googleapis.com/css2?family=Oswald:wght@500;600&family=Montserrat:wght@400;500;600;700;800&display=swap" rel="stylesheet">
<style>
:root{
  --red:#b05a55;
  --blue:#6fb4c9;
  --teal:#4aa3b5;
  --ink:#3a3a3a;
  --stage:#4d4d4d;
  --paper:#ffffff;
  --band:linear-gradient(90deg,var(--red) 0%,var(--blue) 50%,var(--red) 100%);
}
*{box-sizing:border-box;margin:0;padding:0}
html,body{width:1147px;height:1200px;overflow:hidden}
body{background:var(--stage);font-family:"Montserrat",sans-serif;color:var(--ink);position:relative}
.card{position:absolute;top:137px;width:387px;height:896px;background:var(--paper);overflow:hidden}
.card--front{left:161px}
.card--back{left:612px}
.abs{position:absolute}

/* front */
.headline{left:0;right:0;top:22px;text-align:center;font-family:"Oswald",sans-serif;font-weight:600;font-size:29px;letter-spacing:-.3px;line-height:1}
.headline .food{color:var(--red)}
.headline .brain{color:var(--blue)}
.intro{left:27px;right:27px;top:61px;font-size:14px;line-height:19.5px;text-align:justify}
.steps-band{left:20px;right:19px;top:169px;height:32px;background:var(--band);color:#fff;font-family:"Oswald",sans-serif;font-weight:500;font-size:19px;text-align:center;line-height:32px}
.steps{left:22px;right:18px;top:212px;list-style:none;font-size:14px;line-height:19.5px}
.steps li{position:relative;padding-left:27px}
.steps li.tick::before{content:"";position:absolute;left:0;top:3px;width:12px;height:12px;border-radius:50%;background:var(--red)}
.steps li.tick::after{content:"";position:absolute;left:3px;top:6px;width:5px;height:3px;border-left:2px solid #fff;border-bottom:2px solid #fff;transform:rotate(-45deg)}
.collage{left:0;right:0;top:497px;height:182px;background:linear-gradient(90deg,var(--blue),var(--red))}
.photo{position:absolute}
.ph-salmon{left:0;top:6px;width:124px;height:84px;background:linear-gradient(135deg,#c9823e,#8b4a2a 60,#e35a3c)}
.ph-rice{left:130px;top:6px;width:124px;height:84px;background:radial-gradient(circle at 50% 45%,#f1e6c8 0,#f6f3ec 45%,#fdfdfd 70%)}
.ph-chicken{left:262px;top:6px;width:125px;height:84px;background:linear-gradient(135deg,#3a2a22,#7a3b1c 55%,#2a2220)}
.ph-veg{left:0;top:96px;width:190px;height:83px;background:linear-gradient(120deg,#6b2f45,#7b8a3a 45%,#c8412f 75%,#4e6b2c)}
.ph-berries{left:196px;top:96px;width:191px;height:83px;background:linear-gradient(90deg,#f4f4f4,#2a2a35 30%,#4a5f86 55%,#d83040 80%,#f7f7f7)}
.org{display:flex;align-items:center;gap:12px;justify-content:center;left:0;right:0}
.org-mark{width:64px;height:64px;border-radius:50%;background:var(--teal);flex:none}
.org-name{color:var(--teal);font-weight:700;font-size:15px;line-height:17px;text-transform:uppercase;width:180px}
.front-org{top:696px}
.doctor{left:20px;right:20px;top:772px;text-align:center;color:var(--red);font-weight:800;font-size:15px;line-height:19.5px}
.quote{left:24px;right:24px;top:815px;text-align:center;font-size:14px;line-height:19.5px}
.front-foot{left:0;right:0;bottom:0;height:17px;background:var(--red)}

/* back */
.recipe-title{left:0;right:0;top:24px;text-align:center;color:var(--red);font-weight:800;font-size:28px;line-height:1.05}
.recipe-sub{left:0;right:0;top:53px;text-align:center;color:var(--blue);font-weight:700;font-size:16px}
.ph-dish{left:27px;top:85px;width:124px;height:140px;background:linear-gradient(135deg,#e7b56d,#b0552b 50%,#d24a36 75%,#6b3a26)}
.ingr-head{left:159px;top:86px;width:169px;height:20px;background:linear-gradient(90deg,var(--blue),var(--red));color:#fff;font-weight:700;font-size:14px;line-height:20px;padding-left:10px}
.ingr{left:160px;right:10px;top:113px;font-size:14px;line-height:19.5px}
.dot{display:inline-block;width:7px;height:7px;border-radius:50%;background:var(--red);margin:0 4px 1px 0;vertical-align:middle}
.method{left:26px;right:26px;top:241px;font-size:14px;line-height:19.5px;text-align:justify}
.tradition{left:27px;right:27px;top:402px;height:93px;border-radius:20px;background:linear-gradient(90deg,var(--red),var(--blue));color:#fff;font-size:13px;line-height:16px;padding:12px 14px;text-align:justify}
.back-org{top:502px}
.back-org .org-mark{width:62px;height:62px}
.info{left:0;right:0;text-align:center}
.info-h{color:var(--teal);font-weight:800;font-size:20px;top:580px}
.info-s{color:var(--red);font-weight:700;font-size:17px;top:604px}
.link-name{color:var(--teal);font-weight:700;font-size:15px}
.link-url{font-size:14px}
.brain-h{color:var(--teal);font-weight:700;font-size:17px;top:677px}
.brain-s{color:var(--red);font-weight:700;font-size:14px;line-height:19.5px;top:700px}
.funding{left:26px;right:23px;top:817px;font-size:7.3px;line-height:10.5px;text-align:justify;text-align-last:center}
.back-foot{left:0;right:0;bottom:0;height:16px;background:var(--blue)}
</style>
</head>
<body>

<section class="card card--front">
  <h1 class="abs headline"><span class="food">HEALTHY FOOD</span> <span class="brain">HEALTHY BRAIN</span></h1>
  <p class="abs intro">Everyone slows down as they get older, both in body &amp; mind. Eating healthier food can help your overall health, including brain health. It may also reduce your risk for memory loss &amp; problems thinking.</p>
  <h2 class="abs steps-band">Healthier steps to protect your brain:</h2>
  <ul class="abs steps">
    <li class="tick">Eat more vegetables, fruits, whole grains, &amp; lower-fat milk</li>
    <li class="tick">Use less salt &amp; added sugar</li>
    <li class="tick">Eat more fish, chicken, turkey, beans, &amp; nuts</li>
    <li class="tick">Cut down on bad fats (“saturated” &amp; trans), cholesterol, and red meat</li>
    <li class="tick">Buy fresh, not packaged food when you can</li>
    <li class="tick">Limit how much alcohol you drink</li>
    <li class="tick">Learn your daily calorie needs for<br>your body size</li>
    <li class="tick">Take care of your mental and spiritual health to support your physical &amp; brain health</li>
    <li>Small changes can make a<br>big&nbsp; difference for better brain health</li>
  </ul>
  <div class="abs collage">
    <div class="photo ph-salmon" role="img" aria-label="Grilled salmon fillet with tomato and lemon"></div>
    <div class="photo ph-rice" role="img" aria-label="Bowl of cooked brown rice"></div>
    <div class="photo ph-chicken" role="img" aria-label="Roasted chicken wings with herbs"></div>
    <div class="photo ph-veg" role="img" aria-label="Crate of fresh mixed vegetables"></div>
    <div class="photo ph-berries" role="img" aria-label="Blackberry, blueberry and raspberry close-up"></div>
  </div>
  <div class="abs org front-org">
    <span class="org-mark"></span>
    <span class="org-name">Riverstone Resource Center for Brain Health</span>
  </div>
  <p class="abs doctor">TALK TO YOUR DOCTOR ABOUT MORE STEPS TO HEALTHIER FOOD CHOICES.</p>
  <p class="abs quote">“Without the elk, salmon, huckleberries, shell-fish, &amp; cedar trees we are nobody...”Marla Stonecrest (River Valley)</p>
  <div class="abs front-foot"></div>
</section>

<section class="card card--back">
  <h1 class="abs recipe-title">MAKE THIS AT HOME</h1>
  <p class="abs recipe-sub">Grilled Salmon &amp; Veggie Foil Packets</p>
  <div class="abs ph-dish" role="img" aria-label="Grilled salmon topped with tomato slice and thyme"></div>
  <h2 class="abs ingr-head">INGREDIENTS:</h2>
  <div class="abs ingr">
    <div><span class="dot"></span>Salmon <span class="dot"></span>&nbsp;Asparagus</div>
    <div><span class="dot"></span>Red or Green Peppers</div>
    <div style="padding-left:11px">(Or any seasonal vegetable)</div>
    <div><span class="dot"></span>Onion <span class="dot"></span>Lemon – sliced</div>
    <div><span class="dot"></span>Basil &nbsp;<span class="dot"></span>Olive Oil</div>
    <div><span class="dot"></span>Salt and Pepper</div>
  </div>
  <p class="abs method">Cut asparagus, peppers, &amp;&nbsp; onion into bite-size pieces. Cut salmon into 4-6 oz pieces. Tear tin foil large enough to wrap around salmon &amp; veggies (2 layers). Add veggies &amp; salmon to foil. Drizzle with olive oil, season with salt, pepper, basil, garlic &amp; top with a piece of sliced lemon. Wrap foil tightly around food. Grill at 400 degrees for about 20 minutes. Careful opening!</p>
  <p class="abs tradition">Food &amp; drink are a source of strength &amp; connection to community. A return to traditional food pathways &amp; eating local, seasonal fresh foods make healthier eating easier.</p>
  <div class="abs org back-org">
    <span class="org-mark"></span>
    <span class="org-name">Riverstone Resource Center for Brain Health</span>
  </div>
  <h2 class="abs info info-h">FOR MORE INFORMATION</h2>
  <p class="abs info info-s">About Healthier Eating</p>
  <p class="abs info link-name" style="top:632px">PlateWise Guide</p>
  <p class="abs info link-url" style="top:650px">https://www.platewiseguide.org</p>
  <p class="abs info brain-h">About Brain Health</p>
  <p class="abs info brain-s">Riverstone Resource Center for<br>Brain Health</p>
  <p class="abs info link-url" style="top:744px">https://www.riverstonebrainhealth.org</p>
  <p class="abs info link-name" style="top:771px">National Memory Health Program</p>
  <p class="abs info link-url" style="top:790px">https://www.memoryhealthprogram.org</p>
  <p class="abs funding">This product is supported by the Agency for Community Health (ACH) of the National Department of Public Wellness (NDPW) as part of a financial assistance award totaling $348,711 with 100 percent funded by ACH/NDPW. The contents are those of the author(s) and do not necessarily represent the official views of, nor an endorsement, by ACH/NDPW, or the Government.</p>
  <div class="abs back-foot"></div>
</section>

</body>
</html>
```